Etikett für einen Rosé Wein
Zielgruppe
Wir sind ein Weingut und benötigen ein neues Etikett für unseren Muskattrollinger Rosé. Unsere Kunden sind eher traditionelle Weinkäufer.
Aufgabenstellung
Format:
Höhe: 9 cm
Breite: 11 cm
Da es nur ein Vorderetikett gibt, müssen alle relevanten Angaben (Hersteller, Alkohol, Inhalt in L, Rebsorte, etc.) enthalten sein. (siehe Flaschenabbildung anbei)
WÜRTTEMBERG
2019er
Muskattrollinger Rosé
DEUTSCHER QUALITÄTSWEIN
11,0 % Vol.
0,75 l
Enthält Sulfite
A.P.Nr. 58271346
Abfüller
Straße / PLZ / Ort / Tel.
Der Flaschenverschluss ist schwarz d.h. das neue Etikettendesign sollte dazu passen.
Bisher ist der Hintergrund des Weinetiketts schwarz. Dies muss jedoch nicht so bleiben.
Im Anhang finden Sie außerdem ein Plakat. Ggf. können Sie für das Flaschendesign einige nostalgische Elemente davon übernehmen.

```html
<!DOCTYPE html>
<html lang="de">
<head>
<meta charset="utf-8">
<title>Muskattrollinger Rosé – Etikett</title>
<link href="https://fonts.googleapis.com/css2?family=Jost:wght@300;400&family=Great+Vibes&display=swap" rel="stylesheet">
<style>
  :root {
    --label-bg: #000000;
    --ink: #ffffff;
    --leaf-tone-light: #3a3a3a;
    --leaf-tone-dark: #111111;
  }
  html, body {
    margin: 0;
    padding: 0;
    width: 1200px;
    height: 981px;
    overflow: hidden;
    background: var(--label-bg);
  }
  .label {
    position: relative;
    width: 1200px;
    height: 981px;
    background: var(--label-bg);
    color: var(--ink);
    font-family: "Jost", sans-serif;
    font-weight: 300;
  }
  .frame {
    position: absolute;
    inset: 0;
  }
  .region {
    position: absolute;
    left: 0;
    width: 1200px;
    top: 82px;
    text-align: center;
    margin: 0;
    padding-left: 6px;
    font-size: 88px;
    font-weight: 400;
    letter-spacing: 0.07em;
    line-height: 1;
  }
  .variety {
    position: absolute;
    left: 232px;
    top: 180px;
    margin: 0;
    font-family: "Great Vibes", cursive;
    font-weight: 400;
    font-size: 138px;
    line-height: 1;
    white-space: nowrap;
  }
  .style {
    position: absolute;
    left: 548px;
    top: 318px;
    margin: 0;
    font-family: "Great Vibes", cursive;
    font-weight: 400;
    font-size: 196px;
    line-height: 1;
  }
  .leaves {
    position: absolute;
    left: 32px;
    top: 415px;
    width: 522px;
    height: 388px;
    border-radius: 40% 55% 10% 30%;
    background: radial-gradient(ellipse at 55% 55%, var(--leaf-tone-light), var(--leaf-tone-dark) 75%);
  }
  .facts {
    position: absolute;
    right: 83px;
    top: 595px;
    text-align: right;
    line-height: 1;
  }
  .facts-line {
    display: block;
    font-size: 37px;
    font-weight: 400;
    margin-bottom: 14px;
  }
  .quality {
    display: block;
    font-size: 44px;
    font-weight: 400;
    letter-spacing: 0.06em;
    margin-top: 22px;
  }
  .producer {
    position: absolute;
    left: 55px;
    width: 1090px;
    top: 830px;
    text-align: center;
    font-size: 25px;
    font-weight: 400;
    line-height: 39px;
  }
</style>
</head>
<body>
<main class="label">
  <svg class="frame" width="1200" height="981" viewBox="0 0 1200 981" aria-hidden="true">
    <g stroke="#ffffff" stroke-width="3" fill="none">
      <polyline points="232,125 55,125 55,928 1145,928 1145,125 950,125"/>
      <line x1="55" y1="805" x2="1145" y2="805"/>
    </g>
  </svg>

  <h1 class="region">württemberg</h1>
  <p class="variety">Muskattrollinger</p>
  <p class="style">Rosé</p>

  <div class="leaves" role="img" aria-label="Weißgezeichnete Weinblätter in Linienzeichnung"></div>

  <div class="facts">
    <span class="facts-line">2019 · 11 % vol · 0,75 l</span>
    <span class="facts-line">Enthält Sulfite</span>
    <span class="quality">deutscher qualitätswein</span>
  </div>

  <footer class="producer">
    lukas hermann · rebenweg 12 · 71234 lindenbach am berg<br>
    telefon 07131 5820347 · A.P.Nr. 58271346 · abfüller D-BWW612
  </footer>
</main>
</body>
</html>
```